Business Card Design for Varnok Facility Services

We are looking for a Business Card Design for the Company "Varnok Facility Services."
Front side:
- Company Logo (small)
- Company Name, address, pohone, website and personal data.
- white background, for text e.g. company colors (blue or green like in the logo)
Please use following data:
Company data:
Varnok Facility Services Tulbrecht
Kirchmattweg 12
6331 Cham
www.varnok-fs.ch
Person data:
Ruben Tulbrecht
Geschäftsführer
+41 76 519 84 60
info@varnok-fs.ch
Back side:
could be colored in blue or green
please use a big logo sing and some smaller icons to say what is all beeing offered in facility services, like cleaning, maintenance cleaning
industrial cleaning, caretaking, gardening, disposal. There is no need for everyone of the icons if there are similar or an icon is standing for more of them.
Cleaning Service
colors to use:
blue: HEX 246BB0
green: HEX 52B33E

```html
<!DOCTYPE html>
<html lang="de">
<head>
<meta charset="utf-8">
<title>Varnok Facility Services – Visitenkarte</title>
<link rel="stylesheet" href="https://fonts.googleapis.com/css2?family=Lato:wght@400;700&display=swap">
<style>
  :root {
    --brand-blue: #246BB0;
    --brand-green: #3DAF4B;
    --accent-green: #52B33E;
    --text-grey: #555555;
    --paper: #ffffff;
    --backdrop: #e9e7e3;
  }
  * { box-sizing: border-box; margin: 0; padding: 0; }
  html, body {
    width: 1200px; height: 848px; overflow: hidden;
    background: var(--backdrop);
    font-family: "Lato", sans-serif;
  }
  .canvas { position: relative; width: 1200px; height: 848px; }

  .card {
    position: absolute;
    width: 672px; height: 380px;
    box-shadow: 0 4px 14px rgba(0,0,0,0.18);
  }
  .card--front { left: 251px; top: 28px; background: var(--paper); }
  .card--back  { left: 251px; top: 442px; background: var(--brand-green); }

  /* Front */
  .brand-mark {
    position: absolute; display: flex; align-items: center; gap: 10px;
    font-weight: 700; white-space: nowrap;
  }
  .card--front .brand-mark {
    right: 37px; top: 70px;
    font-size: 26px; color: var(--brand-blue);
  }
  .brand-dot { width: 14px; height: 14px; border-radius: 50%; background: currentColor; flex: none; }

  .person { position: absolute; left: 38px; top: 212px; }
  .person__name { font-size: 21px; font-weight: 700; color: var(--accent-green); line-height: 1.1; }
  .person__role { font-size: 18px; color: var(--text-grey); line-height: 1.3; }
  .rule {
    position: absolute; left: 182px; right: 37px; top: 248px;
    height: 1.5px; background: var(--accent-green);
  }

  .contact { position: absolute; left: 38px; top: 279px; list-style: none; }
  .contact li {
    display: flex; align-items: center; gap: 8px;
    font-size: 18px; color: var(--text-grey); height: 23px;
  }
  .contact svg { width: 12px; height: 12px; fill: var(--accent-green); flex: none; }

  .address {
    position: absolute; right: 37px; top: 301px;
    font-style: normal; text-align: right;
    font-size: 18px; color: var(--text-grey); line-height: 23px;
  }

  /* Back */
  .card--back .brand-mark {
    left: 0; right: 0; justify-content: center; top: 104px;
    font-size: 36px; color: var(--paper);
  }
  .card--back .brand-dot { width: 20px; height: 20px; }

  .services { position: absolute; left: 0; right: 0; top: 236px; text-align: center; color: var(--paper); }
  .services__title {
    display: inline-block; font-size: 25px; font-weight: 700;
    padding: 0 6px 4px; border-bottom: 2px solid var(--paper);
  }
  .services__list { list-style: none; margin-top: 14px; font-size: 21px; }
  .services__row { display: flex; justify-content: center; gap: 14px; line-height: 31px; }
  .services__row span::before {
    content: ""; display: inline-block; width: 11px; height: 11px;
    border-radius: 50%; background: var(--paper); margin-right: 10px;
    vertical-align: middle; position: relative; top: -2px;
  }
</style>
</head>
<body>
<main class="canvas">

  <section class="card card--front" aria-label="Vorderseite">
    <div class="brand-mark"><span class="brand-dot"></span>Varnok Facility Services</div>

    <div class="person">
      <p class="person__name">Ruben Tulbrecht</p>
      <p class="person__role">Geschäftsführer</p>
    </div>
    <div class="rule"></div>

    <ul class="contact">
      <li>
        <svg viewBox="0 0 24 24" aria-hidden="true"><path d="M6.6 10.8a15.1 15.1 0 0 0 6.6 6.6l2.2-2.2a1 1 0 0 1 1-.25 11.4 11.4 0 0 0 3.6.57 1 1 0 0 1 1 1V20a1 1 0 0 1-1 1A17 17 0 0 1 3 4a1 1 0 0 1 1-1h3.5a1 1 0 0 1 1 1c0 1.25.2 2.45.57 3.57a1 1 0 0 1-.25 1z"/></svg>
        +41 76 519 84 60
      </li>
      <li>
        <svg viewBox="0 0 24 24" aria-hidden="true"><path d="M2 5h20v14H2z M2 5l10 8 10-8" fill="var(--accent-green)"/><path d="M3 6l9 7 9-7" fill="none" stroke="#fff" stroke-width="2"/></svg>
        info@varnok-fs.ch
      </li>
      <li>
        <svg viewBox="0 0 24 24" aria-hidden="true"><circle cx="12" cy="12" r="10"/><path d="M2 12h20M12 2c3 3 3 17 0 20M12 2c-3 3-3 17 0 20M4 7h16M4 17h16" fill="none" stroke="#fff" stroke-width="1.4"/></svg>
        www.varnok-fs.ch
      </li>
    </ul>

    <address class="address">Kirchmattweg 12<br>6331 Cham</address>
  </section>

  <section class="card card--back" aria-label="Rückseite">
    <div class="brand-mark"><span class="brand-dot"></span>Varnok Facility Services</div>

    <div class="services">
      <h2 class="services__title">Services</h2>
      <div class="services__list">
        <div class="services__row"><span>Maintenance cleaning</span><span>Industrial cleaning</span></div>
        <div class="services__row"><span>Cleaning</span><span>Caretaking</span><span>Gardening, disposal</span></div>
      </div>
    </div>
  </section>

</main>
</body>
</html>
```